Business cards and Stationary for Bright Learning Alliance
A Chinese Education Consulting Company
Business cards and Stationary for Bright Learning Alliance - Education
Creative Brief
Professional
Dennis R. Tolwy
Manager
7214 Marlow Court, San Ramon, CA 94583
dennistolwy@brilearnal.com
www.brilearnal.com
Please leave abundant space for multi address, (2) multi cell phones (3)

```html
<!DOCTYPE html>
<html lang="en">
<head>
<meta charset="utf-8">
<title>Bright Learning Alliance — Stationery</title>
<link href="https://fonts.googleapis.com/css2?family=Lora:wght@400;600&display=swap" rel="stylesheet">
<style>
  :root {
    --stage: #e7e4e0;
    --paper: #ffffff;
    --paper-edge: #dcd8d3;
    --crimson: #b3121b;
    --crimson-dark: #7d0b10;
    --gold: #c9a04a;
    --gold-light: #ecd79a;
    --ink: #4a4a4a;
    --ink-soft: #8a8a8a;
    --faint: #f1e6e6;
  }
  * { box-sizing: border-box; margin: 0; padding: 0; }
  html, body { width: 1200px; height: 466px; overflow: hidden; }
  body { background: var(--stage); font-family: "Lora", Georgia, serif; color: var(--ink); position: relative; }

  .sheet { position: absolute; background: var(--paper); box-shadow: 0 1px 3px rgba(0,0,0,.18); }

  .brand { display: flex; align-items: center; gap: 4px; color: var(--crimson); font-weight: 600; white-space: nowrap; }
  .brand-dot { width: 9px; height: 9px; border-radius: 50%; background: var(--crimson); flex: none; }

  /* Business cards */
  .card { width: 60px; height: 36px; left: 7px; overflow: hidden; }
  .card-front { top: 156px; }
  .card-front .band { position: absolute; right: 0; top: 0; bottom: 0; width: 14px; background: linear-gradient(180deg, var(--crimson), var(--crimson-dark)); clip-path: ellipse(100% 80% at 100% 50%); }
  .card-front .brand { position: absolute; left: 4px; top: 6px; font-size: 2.5px; gap: 2px; z-index: 1; }
  .card-front .brand-dot { width: 5px; height: 5px; }
  .card-front .person { position: absolute; left: 4px; bottom: 5px; font-size: 2.2px; line-height: 1.3; z-index: 1; }
  .card-back { top: 199px; display: flex; justify-content: center; align-items: center; }
  .card-back .brand { font-size: 3px; gap: 2px; }
  .card-back .brand-dot { width: 6px; height: 6px; }
  .card-back::after { content: ""; position: absolute; left: 0; right: 0; bottom: 0; height: 3px; background: var(--crimson); }

  /* Letterheads */
  .letterhead { top: 43px; width: 308px; height: 420px; }
  .letterhead-one { left: 90px; }
  .letterhead-two { left: 420px; }
  .letterhead .brand { position: absolute; top: 14px; left: 50%; transform: translateX(-50%); font-size: 8px; }
  .letterhead .faint-mark { position: absolute; top: 140px; left: 50%; transform: translateX(-50%); color: var(--faint); font-weight: 600; font-size: 17px; white-space: nowrap; }
  .contact { position: absolute; font-size: 4.4px; line-height: 1.6; color: var(--ink-soft); }
  .contact span { display: flex; align-items: center; gap: 2px; }
  .contact svg { width: 4px; height: 4px; fill: var(--crimson); }
  .letterhead-one .contact { left: 22px; bottom: 22px; }
  .letterhead-two .contact { left: 0; right: 0; bottom: 22px; display: flex; justify-content: center; gap: 8px; }

  /* Envelopes */
  .envelope-red { left: 763px; top: 30px; width: 330px; height: 145px; overflow: hidden; }
  .envelope-red .flap { position: absolute; inset: 0 0 auto 0; height: 64px; background: linear-gradient(180deg, #d21a22, var(--crimson-dark)); }
  .envelope-gold { left: 763px; top: 178px; width: 330px; height: 72px; background: linear-gradient(120deg, var(--gold-light), var(--gold) 55%, #a67e2e); }
  .envelope-white { left: 772px; top: 252px; width: 318px; height: 112px; }
  .envelope-white::before { content: ""; position: absolute; inset: 0; background: #fafafa; clip-path: polygon(0 0, 50% 38%, 100% 0); }
  .envelope-white .brand { position: absolute; left: 50%; top: 64px; transform: translateX(-50%); font-size: 7px; z-index: 1; }
  .envelope-front { left: 775px; top: 380px; width: 312px; height: 82px; }
  .envelope-front .brand { position: absolute; left: 12px; top: 10px; font-size: 6px; }
  .envelope-front .return { position: absolute; left: 12px; top: 24px; font-size: 4.2px; color: var(--ink-soft); line-height: 1.5; }
</style>
</head>
<body>

  <div class="sheet card card-front">
    <div class="band"></div>
    <div class="brand"><i class="brand-dot"></i>Bright Learning Alliance</div>
    <div class="person">Dennis R. Tolwy<br>Manager<br>dennistolwy@brilearnal.com</div>
  </div>
  <div class="sheet card card-back">
    <div class="brand"><i class="brand-dot"></i>Bright Learning Alliance</div>
  </div>

  <div class="sheet letterhead letterhead-one">
    <div class="brand"><i class="brand-dot"></i>Bright Learning Alliance</div>
    <div class="faint-mark">Bright Learning Alliance</div>
    <div class="contact">
      <span><svg viewBox="0 0 10 10"><circle cx="5" cy="5" r="5"/></svg>7214 Marlow Court, San Ramon, CA 94583</span>
      <span><svg viewBox="0 0 10 10"><circle cx="5" cy="5" r="5"/></svg>Phone (925) 555-0147</span>
      <span><svg viewBox="0 0 10 10"><circle cx="5" cy="5" r="5"/></svg>dennistolwy@brilearnal.com</span>
      <span><svg viewBox="0 0 10 10"><circle cx="5" cy="5" r="5"/></svg>www.brilearnal.com</span>
    </div>
  </div>

  <div class="sheet letterhead letterhead-two">
    <div class="brand"><i class="brand-dot"></i>Bright Learning Alliance</div>
    <div class="faint-mark">Bright Learning Alliance</div>
    <div class="contact">
      <span><svg viewBox="0 0 10 10"><circle cx="5" cy="5" r="5"/></svg>(925) 555-0147</span>
      <span><svg viewBox="0 0 10 10"><circle cx="5" cy="5" r="5"/></svg>dennistolwy@brilearnal.com</span>
      <span><svg viewBox="0 0 10 10"><circle cx="5" cy="5" r="5"/></svg>www.brilearnal.com</span>
    </div>
  </div>

  <div class="sheet envelope-red"><div class="flap"></div></div>
  <div class="sheet envelope-gold"></div>
  <div class="sheet envelope-white">
    <div class="brand"><i class="brand-dot"></i>Bright Learning Alliance</div>
  </div>
  <div class="sheet envelope-front">
    <div class="brand"><i class="brand-dot"></i>Bright Learning Alliance</div>
    <div class="return">7214 Marlow Court<br>San Ramon, CA 94583</div>
  </div>

</body>
</html>
```